LumaLearn.net the Free Online Tutorial Needs a New Web Design

We need a new web design for our existing website, LumaLearn.net. We provide a Free Online Tutorial of any code, like HTML, CSS, PHP, Jquery, javascript etc, including online editor.
We would like to see designs that interesting, simple, interactive, and be a very comfortable place to read in a long time.
We need 2 pages design for:
1. Home Page (http://lumalearn.net) and
2. Listing Page (http://lumalearn.net/tutorial/833/sql/sql-basics/sql-and-or-operator.html)
For Listing Page We need nice "Left Menu" at left side and Content Page (min 728px) at right side.
I need File PSD and/or Vector Only, without HTML code.

```html
<!DOCTYPE html>
<html lang="en">
<head>
<meta charset="utf-8">
<title>LumaLearn – Free Online Tutorials</title>
<link rel="stylesheet" href="https://fonts.googleapis.com/css2?family=Open+Sans:wght@400;600;700;800&display=swap">
<style>
  :root {
    --blue: #0a73cb;
    --green: #6aaf44;
    --red: #f1514e;
    --yellow: #fdb714;
    --ink: #222222;
    --text: #444444;
    --muted: #666666;
    --band: #f0f0f0;
    --rule: #cfcfcf;
    --dark-bar: #4b4b4b;
    --white: #ffffff;
  }
  * { box-sizing: border-box; margin: 0; padding: 0; }
  html, body { width: 1200px; height: 1200px; overflow: hidden; background: var(--white); }
  body { font-family: "Open Sans", Arial, sans-serif; color: var(--text); position: relative; }

  .login-bar { position: absolute; left: 200px; top: 0; width: 800px; height: 43px; display: flex; }
  .login-bar > div { width: 200px; height: 43px; display: flex; align-items: center; justify-content: center; }
  .login-label { background: var(--blue); color: var(--white); font-size: 15px; letter-spacing: .5px; }
  .field-user { background: var(--green); }
  .field-pass { background: var(--red); }
  .field { width: 186px; height: 29px; background: var(--white); border: none; font: 11px "Open Sans", sans-serif; color: #888; padding: 0 10px; display: flex; align-items: center; }
  .signup { background: var(--yellow); color: var(--white); font-size: 14px; letter-spacing: .5px; }

  .hero { position: absolute; left: 200px; top: 60px; width: 800px; height: 333px; }
  .hero svg { position: absolute; left: 0; top: 0; }
  .brand { position: absolute; left: 20px; top: 12px; display: flex; align-items: center; gap: 8px; color: var(--white); font-size: 27px; font-weight: 600; letter-spacing: -0.5px; }
  .brand-mark { width: 24px; height: 24px; background: var(--white); }
  .hero-copy { position: absolute; right: 0; top: 235px; width: 600px; text-align: right; }
  .hero-title { font-size: 19px; color: var(--ink); font-weight: 400; margin-bottom: 4px; }
  .hero-text { font-size: 10.4px; line-height: 14px; color: var(--text); text-align: justify; text-align-last: right; padding-left: 6px; }
  .hero-button { position: absolute; right: 0; top: 304px; width: 84px; height: 29px; background: #2b2b2b; color: var(--white); font-size: 10.5px; display: flex; align-items: center; justify-content: center; }

  .feature-band { position: absolute; left: 0; top: 408px; width: 1200px; height: 388px; background: var(--band); border-top: 2px solid var(--rule); border-bottom: 2px solid var(--rule); }
  .topic-menu { position: absolute; left: 197px; top: 13px; width: 205px; list-style: none; }
  .topic-menu li { height: 39px; margin-bottom: 4.3px; border: 2px solid #c8c8c8; background: var(--white); font-size: 13px; color: var(--ink); display: flex; align-items: center; padding-left: 44px; letter-spacing: .3px; }
  .feature-title { position: absolute; left: 436px; top: 22px; font-size: 27px; font-weight: 700; color: var(--ink); letter-spacing: .5px; }
  .tile { position: absolute; width: 275px; height: 127px; color: var(--white); display: flex; flex-direction: column; align-items: center; justify-content: center; text-align: center; }
  .tile-name { font-size: 25px; font-weight: 700; line-height: 24px; }
  .tile-sub { font-size: 12px; font-weight: 700; letter-spacing: .6px; margin-top: 2px; }
  .tile-html5 { left: 435px; top: 73px; background: var(--blue); }
  .tile-canvas { left: 725px; top: 73px; background: var(--green); }
  .tile-sql { left: 435px; top: 223px; background: var(--red); }
  .tile-code { left: 725px; top: 223px; background: var(--yellow); }
  .tile-canvas .tile-name, .tile-sql .tile-name { font-size: 24px; }
  .tile-code .tile-name { font-size: 22px; line-height: 22px; }

  .link-columns { position: absolute; top: 815px; left: 0; width: 1200px; }
  .link-col { position: absolute; width: 165px; list-style: none; }
  .link-col h3 { font-size: 13.5px; font-weight: 400; margin-bottom: 1px; }
  .link-col li { font-size: 10.4px; line-height: 13.4px; white-space: nowrap; }
  .col-js { left: 203px; color: var(--blue); }
  .col-tryit { left: 373px; color: var(--green); }
  .col-html5 { left: 536px; top: 3px; color: var(--red); }
  .col-canvas { left: 711px; top: 3px; color: var(--yellow); }
  .col-articles { left: 859px; top: 5px; color: var(--ink); }

  .footer-bar { position: absolute; left: 0; top: 987px; width: 1200px; height: 7px; background: var(--dark-bar); }
  .footer-nav { position: absolute; left: 0; top: 1006px; width: 1200px; display: flex; justify-content: center; gap: 22px; font-size: 10.5px; color: var(--muted); list-style: none; }
  .footer-copy { position: absolute; left: 0; top: 1026px; width: 1200px; text-align: center; font-size: 10.5px; color: var(--muted); }
</style>
</head>
<body>

<header class="login-bar">
  <div class="login-label">LOGIN HERE</div>
  <div class="field-user"><span class="field">Username</span></div>
  <div class="field-pass"><span class="field"></span></div>
  <div class="signup">NEW USER? SIGN UP HERE</div>
</header>

<section class="hero">
  <svg width="800" height="333" viewBox="0 0 800 333" role="img" aria-label="Photo of smiling students working together at computers in a classroom">
    <defs>
      <linearGradient id="heroPhoto" x1="0" y1="0" x2="1" y2="1">
        <stop offset="0" stop-color="#3c4a5c"/>
        <stop offset="0.35" stop-color="#6a5a58"/>
        <stop offset="0.6" stop-color="#2c3440"/>
        <stop offset="1" stop-color="#1c2028"/>
      </linearGradient>
    </defs>
    <polygon points="3,0 800,0 3,333" fill="url(#heroPhoto)"/>
  </svg>
  <div class="brand"><span class="brand-mark"></span>LumaLearn</div>
  <div class="hero-copy">
    <h1 class="hero-title">The Free Online Tutorials Place</h1>
    <p class="hero-text">for Learning, testing, and examples for web building. The Examples in each chapter might be simplified to improve your basic understanding. With LumaLearn You will feel much easier than ever to learn about HTML including online code editor for each chapter, so you can edit, modify and execute the codecan edit, modify and execute the code.</p>
  </div>
  <div class="hero-button">Know more</div>
</section>

<section class="feature-band">
  <ul class="topic-menu">
    <li>HTML</li><li>CSS</li><li>JAVASCRIPT</li><li>PHP</li>
    <li>SQL</li><li>JQUERY</li><li>JSON</li><li>MORE..</li>
  </ul>
  <h2 class="feature-title">FEATURED TRYIT YOURSELF</h2>
  <div class="tile tile-html5"><span class="tile-name">HTML5</span><span class="tile-sub">TUTORIAL</span></div>
  <div class="tile tile-canvas"><span class="tile-name">HTML<br>5 CANVAS</span><span class="tile-sub">TUTORIAL</span></div>
  <div class="tile tile-sql"><span class="tile-name">SQL</span><span class="tile-sub">TUTORIAL</span></div>
  <div class="tile tile-code"><span class="tile-name">ONLINE CODE</span><span class="tile-sub">TUTORIAL</span></div>
</section>

<nav class="link-columns">
  <ul class="link-col col-js">
    <h3>Random Javascript</h3>
    <li>Javascript Looping</li><li>JS String-HTML italics()</li><li>JS DOM Input FileUpload</li>
    <li>JS Global encodeURI()</li><li>JS Number valueOf()</li><li>JS Math pow(x,y)</li>
    <li>Javascript Array Concat()</li><li>JS Number toExponential()</li><li>JS DOM Meta</li>
    <li>JS Number Positive_Infini..</li>
  </ul>
  <ul class="link-col col-tryit">
    <h3>Random Try it</h3>
    <li>Heading with CSS styled</li><li>Colors RGB in HTML</li><li>aside tag example</li>
    <li>tt tag example</li><li>br tag example</li><li>title tag example</li>
    <li>Entities and Symbol HTML</li><li>rp tag example</li><li>datalist tag example</li>
    <li>canvas draw gradient exam..</li>
  </ul>
  <ul class="link-col col-html5">
    <h3>Random HTML5</h3>
    <li>sup tag in html5</li><li>Geolocation</li><li>img html5</li><li>p in html5</li>
    <li>Button Tag is used to def..</li><li>textarea html5</li><li>Text Formating Overview i..</li>
    <li>h5 in html5</li><li>menu html5</li><li>List Overview html5</li>
  </ul>
  <ul class="link-col col-canvas">
    <h3>Random Canvas</h3>
    <li>Canvas Polyline</li><li>Canvas Radial Gradient</li><li>Canvas Draw Images</li>
    <li>Canvas Arc</li><li>Canvas Line</li><li>Canvas Semicircles</li><li>Canvas Line Cap</li>
    <li>Canvas Introduction</li><li>Canvas Bezier Curve</li><li>Canvas Line Width</li>
  </ul>
  <ul class="link-col col-articles">
    <h3>Random Articles</h3>
    <li>How to make WHOIS lookups..</li><li>How to Auto Select All Te..</li><li>How to Make SQL Syntax Hi..</li>
    <li>Changing text with innerh..</li><li>How to Make Drop Down Men..</li><li>Create Transparency Anima..</li>
    <li>Make A lot of Circle Anim..</li><li>How to get an input text ..</li><li>How to Make Drop Down Men..</li>
    <li>How to Make Sitemap.xml</li>
  </ul>
</nav>

<div class="footer-bar"></div>
<ul class="footer-nav">
  <li>Tutorial</li><li>Articles</li><li>Try it</li><li>Canvas</li><li>Webtools</li><li>About</li>
  <li>Terms</li><li>Privacy</li><li>Disclaimer</li><li>Contact</li><li>FAQ</li><li>Find Us on Circlebook</li>
</ul>
<p class="footer-copy">LumaLearn © 2015, All rights reserved</p>

</body>
</html>
```